Everything fresh, everything new

When I take over the practice, I would like to breathe new life into the practice. I want a business card design that catches the eye and brings a breath of fresh air

```html
<!DOCTYPE html>
<html lang="en">
<head>
<meta charset="utf-8">
<title>Bewegraum – Business Card</title>
<link rel="stylesheet" href="https://fonts.googleapis.com/css2?family=Montserrat:wght@500;800&family=Arimo:wght@400&display=swap">
<style>
  :root {
    --green: #8bc540;
    --white: #ffffff;
    --ink: #1d1d1d;
    --ink-soft: #4a4a4a;
    --backdrop: #e9ebe6;
  }
  * { box-sizing: border-box; margin: 0; padding: 0; }
  html, body { width: 1200px; height: 880px; overflow: hidden; }
  body {
    background: var(--backdrop);
    display: flex;
    flex-direction: column;
    align-items: center;
    justify-content: center;
    gap: 40px;
    font-family: "Arimo", Arial, sans-serif;
  }
  .card {
    position: relative;
    width: 640px;
    height: 366px;
    box-shadow: 0 6px 18px rgba(0,0,0,.18);
  }
  .card--front {
    background: var(--green);
    display: flex;
    align-items: center;
    justify-content: center;
  }
  .brand {
    display: flex;
    align-items: center;
    gap: 14px;
    font-family: "Montserrat", sans-serif;
    font-weight: 500;
    letter-spacing: .5px;
  }
  .brand__dot {
    width: 18px; height: 18px;
    border-radius: 50%;
  }
  .card--front .brand { color: var(--white); font-size: 52px; }
  .card--front .brand__dot { background: var(--white); width: 26px; height: 26px; }

  .card--back { background: var(--white); }
  .card--back .brand {
    position: absolute;
    left: 48px; top: 146px;
    color: var(--ink-soft);
    font-size: 32px;
  }
  .card--back .brand__dot { background: var(--green); }
  .divider {
    position: absolute;
    left: 340px; top: 92px;
    width: 2px; height: 150px;
    background: var(--green);
  }
  .contact {
    position: absolute;
    left: 362px; top: 86px;
  }
  .contact__name {
    font-family: "Montserrat", sans-serif;
    font-weight: 800;
    font-size: 24px;
    color: var(--green);
    letter-spacing: .5px;
  }
  .contact__role {
    font-size: 16px;
    color: var(--ink);
    margin: 4px 0 16px;
  }
  .contact__list { list-style: none; }
  .contact__item {
    display: flex;
    align-items: center;
    gap: 10px;
    font-size: 15px;
    color: var(--ink);
    margin-bottom: 8px;
  }
  .contact__icon { width: 16px; height: 16px; flex: none; }
  .address {
    position: absolute;
    left: 0; right: 0; bottom: 56px;
    text-align: center;
    font-size: 18px;
    color: var(--ink);
  }
</style>
</head>
<body>

  <section class="card card--front">
    <div class="brand">
      <span class="brand__dot"></span>
      <span class="brand__name">Bewegraum</span>
    </div>
  </section>

  <section class="card card--back">
    <div class="brand">
      <span class="brand__dot"></span>
      <span class="brand__name">Bewegraum</span>
    </div>

    <div class="divider"></div>

    <div class="contact">
      <h1 class="contact__name">LENA HARTWIG</h1>
      <p class="contact__role">Co-Founder</p>
      <ul class="contact__list">
        <li class="contact__item">
          <svg class="contact__icon" viewBox="0 0 16 16" aria-hidden="true">
            <path fill="#8bc540" d="M3 1.5l2.5-.5 1.5 3.5-1.6 1.1a8 8 0 0 0 5 5l1.1-1.6 3.5 1.5-.5 2.5c-.3 1-1.2 1.5-2.2 1.4C6.4 13.7 2.3 9.6 1.6 3.7 1.5 2.7 2 1.8 3 1.5z"/>
          </svg>
          555-014-2290
        </li>
        <li class="contact__item">
          <svg class="contact__icon" viewBox="0 0 16 16" aria-hidden="true">
            <rect x="1" y="3" width="14" height="10" rx="1" fill="#8bc540"/>
            <path d="M1.5 3.8L8 9l6.5-5.2" fill="none" stroke="#fff" stroke-width="1.3"/>
          </svg>
          info@bewegraum-mail.com
        </li>
        <li class="contact__item">
          <svg class="contact__icon" viewBox="0 0 16 16" aria-hidden="true">
            <circle cx="8" cy="8" r="7" fill="#8bc540"/>
            <path d="M1 8h14M8 1c-2.5 2-2.5 12 0 14M8 1c2.5 2 2.5 12 0 14" fill="none" stroke="#fff" stroke-width="1"/>
          </svg>
          www.bewegraum-web.com
        </li>
      </ul>
    </div>

    <p class="address">P.O. BOX 42-07 LND-3 Linden Ave 14, Fairmont</p>
  </section>

</body>
</html>
```